Velmora and Co Business Card Design

Looking for a business card design. Wanting Smart, Clean and Sharp looking to promote Velmora and Co, our Import Export Business - like Black, White and natural textures. I have uploaded our logo. I like a rounded font but open to other ideas
Being that we have a wide range of products on offer we are looking for a neutral yet eye catching card. We would also like to have Import - Export on the business card to be clear on want our business does.

Target Market(s)

Import export market

Industry/Entity Type

Importer

Contact Information for Business Card

Mr Tobias Kernwell
tobias.kernwell@velmoraandco.com.au
+61 (0) 417 630 284
www.velmoraandco.com.au

Font styles to use
Other font styles liked:
• Unsure of actual font name but something rounded and clean

Colors

Designer to choose colors to be used in the design.

Requirements
Must have
• Instagram icon
• Facebook icon

```html
<!DOCTYPE html>
<html lang="en">
<head>
<meta charset="utf-8">
<title>Velmora and Co Business Card</title>
<link href="https://fonts.googleapis.com/css2?family=Ubuntu:wght@400;500;700&display=swap" rel="stylesheet">
<style>
  :root {
    --ink: #161616;
    --card-black: #1c1c1c;
    --paper: #ffffff;
    --muted: #4a4a4a;
    --soft: #bdbdbd;
    --backdrop: #2b2b2b;
  }
  * { box-sizing: border-box; margin: 0; padding: 0; }
  html, body { width: 1200px; height: 895px; overflow: hidden; }
  body {
    background: var(--backdrop);
    font-family: "Ubuntu", Arial, sans-serif;
    position: relative;
  }
  .card {
    position: absolute;
    left: 250px;
    width: 700px;
    height: 400px;
    box-shadow: 0 10px 30px rgba(0,0,0,.45);
    overflow: hidden;
  }
  .card-front { top: 28px; background: var(--card-black); }
  .card-back { top: 467px; display: flex; }

  .brand {
    display: flex;
    align-items: center;
    gap: 14px;
    color: var(--paper);
    font-weight: 700;
    letter-spacing: 1px;
    text-transform: uppercase;
    white-space: nowrap;
  }
  .brand-square {
    width: 22px; height: 22px;
    background: var(--paper);
    flex: none;
  }
  .card-front .brand {
    position: absolute;
    top: 150px; left: 0; right: 0;
    justify-content: center;
    font-size: 38px;
  }
  .trade-line {
    position: absolute;
    top: 212px; left: 0; right: 0;
    text-align: center;
    color: var(--soft);
    font-size: 14px;
    font-weight: 500;
    letter-spacing: 5px;
    text-transform: uppercase;
  }
  .front-url {
    position: absolute;
    bottom: 58px; left: 0; right: 0;
    text-align: center;
    color: var(--paper);
    font-size: 17px;
    font-weight: 500;
    letter-spacing: 2.5px;
  }

  .back-details {
    width: 400px;
    background: var(--paper);
    padding: 140px 0 0 40px;
    color: var(--ink);
  }
  .person-name {
    font-size: 25px;
    font-weight: 700;
    letter-spacing: .5px;
    text-transform: uppercase;
    white-space: nowrap;
  }
  .person-title {
    font-size: 15px;
    color: var(--muted);
    margin-top: 2px;
  }
  .contact-list {
    list-style: none;
    margin-top: 30px;
    font-size: 15px;
    color: var(--ink);
  }
  .contact-list li {
    display: flex;
    align-items: center;
    gap: 12px;
    margin-bottom: 8px;
    white-space: nowrap;
  }
  .contact-list svg { width: 14px; height: 14px; flex: none; fill: var(--ink); }
  .social-row {
    display: flex;
    gap: 10px;
    margin-top: 14px;
  }
  .social-dot {
    width: 22px; height: 22px;
    border-radius: 50%;
    background: var(--ink);
  }
  .back-brand-panel {
    flex: 1;
    background: var(--card-black);
    display: flex;
    flex-direction: column;
    align-items: center;
    justify-content: center;
    gap: 12px;
  }
  .back-brand-panel .brand { font-size: 22px; gap: 10px; }
  .back-brand-panel .brand-square { width: 16px; height: 16px; }
  .back-brand-panel .trade-tag {
    color: var(--soft);
    font-size: 12px;
    font-weight: 500;
    letter-spacing: 4px;
    text-transform: uppercase;
  }
</style>
</head>
<body>
  <section class="card card-front">
    <div class="brand"><span class="brand-square"></span><span>Velmora and Co</span></div>
    <p class="trade-line">Import - Export</p>
    <p class="front-url">www.velmoraandco.com.au</p>
  </section>

  <section class="card card-back">
    <div class="back-details">
      <h1 class="person-name">Mr Tobias Kernwell</h1>
      <p class="person-title">Founder &amp; CEO</p>
      <ul class="contact-list">
        <li>
          <svg viewBox="0 0 24 24" aria-hidden="true"><path d="M6.6 10.8a15.1 15.1 0 0 0 6.6 6.6l2.2-2.2c.3-.3.7-.4 1-.2 1.1.4 2.3.6 3.6.6.6 0 1 .4 1 1V20c0 .6-.4 1-1 1A17 17 0 0 1 3 4c0-.6.4-1 1-1h3.5c.6 0 1 .4 1 1 0 1.3.2 2.5.6 3.6.1.3 0 .7-.2 1z"/></svg>
          <span>+61 (0) 417 630 284</span>
        </li>
        <li>
          <svg viewBox="0 0 24 24" aria-hidden="true"><path d="M2 5h20v14H2z M4 7v.4l8 5.3 8-5.3V7l-8 5.3z" fill-rule="evenodd"/></svg>
          <span>tobias.kernwell@velmoraandco.com.au</span>
        </li>
        <li>
          <svg viewBox="0 0 24 24" aria-hidden="true"><path d="M12 2a10 10 0 1 0 0 20 10 10 0 0 0 0-20zm6.9 6h-3a15.6 15.6 0 0 0-1.3-3.9A8 8 0 0 1 18.9 8zM12 4c.8 1.2 1.5 2.5 1.9 4h-3.8c.4-1.5 1.1-2.8 1.9-4zM4.3 14a8 8 0 0 1 0-4h3.4a16 16 0 0 0 0 4zm.8 2h3a15.6 15.6 0 0 0 1.3 3.9A8 8 0 0 1 5.1 16zm3-8h-3a8 8 0 0 1 4.3-3.9C8.8 5.3 8.4 6.6 8.1 8zM12 20c-.8-1.2-1.5-2.5-1.9-4h3.8c-.4 1.5-1.1 2.8-1.9 4zm2.3-6H9.7a14.7 14.7 0 0 1 0-4h4.6a14.7 14.7 0 0 1 0 4zm.3 5.9c.6-1.2 1-2.5 1.3-3.9h3a8 8 0 0 1-4.3 3.9zM16.3 14a16 16 0 0 0 0-4h3.4a8 8 0 0 1 0 4z"/></svg>
          <span>www.velmoraandco.com.au</span>
        </li>
      </ul>
      <div class="social-row">
        <span class="social-dot" role="img" aria-label="Photo sharing network icon"></span>
        <span class="social-dot" role="img" aria-label="Social network icon"></span>
      </div>
    </div>
    <div class="back-brand-panel">
      <div class="brand"><span class="brand-square"></span><span>Velmora and Co</span></div>
      <p class="trade-tag">Import - Export</p>
    </div>
  </section>
</body>
</html>
```